Mergers and Acquisitions Business Seeks Fresh Website Design

IMPORTANT: Please only design the Homepage, for the contest. If you win the contest, you will design the inner pages, as see in the attached document 'Brevka 2025 website wireframes."
Design a new website for Brevka at brevka.global. Maintaining current Impact and Open Sans fonts, or using open-source alternatives from Google Fonts.
Enhance the design with a premium feel, impactful visuals, and dynamic content. We want the new design to focus on generating high-quality inquiries, strong calls to action, and consistent branding.
Industry/Entity Type
Mergers and Acquisitions
Number of Pages Required
5+ page
Font styles to use
Other font styles liked:
- See Website Brief file
Requirements
Must have
- Consistency in layout, colours, fonts and overall design
Should not have
- Very bright colours, hard to read fonts, unlicensed images and fonts

```html
<!DOCTYPE html>
<html lang="en">
<head>
<meta charset="utf-8">
<title>Brevka – Deal Origination for Acquirers</title>
<link rel="stylesheet" href="https://fonts.googleapis.com/css2?family=Archivo:wght@400;500;600;700;800&family=Open+Sans:wght@400;600;700&display=swap">
<style>
:root{
  --purple:#5b2a80;
  --purple-dark:#3f1b5c;
  --purple-mid:#7a3fa8;
  --purple-soft:#9b6fc0;
  --gold:#f2b705;
  --gold-deep:#d99a1e;
  --ink:#3a3a3a;
  --muted:#6d6d6d;
  --grey:#f3f3f4;
  --line:#d9d2e0;
  --white:#ffffff;
}
*{box-sizing:border-box;margin:0;padding:0}
html,body{width:1200px;height:5329px;overflow:hidden}
body{font-family:"Open Sans",Arial,sans-serif;color:var(--ink);background:var(--white);position:relative}
.abs{position:absolute}
h1,h2,h3,h4{font-family:"Archivo",Arial,sans-serif;font-weight:500}
.btn{display:inline-block;background:var(--purple);color:var(--white);font-family:"Open Sans",sans-serif;font-size:10px;font-weight:600;border-radius:20px;padding:0 18px;height:30px;line-height:30px;text-decoration:none;text-align:center}

/* header */
.site-header{position:absolute;left:0;top:0;width:1200px;height:62px;background:var(--white)}
.brand{position:absolute;left:105px;top:12px;font-family:"Archivo",sans-serif;font-weight:800;font-size:32px;color:var(--purple);letter-spacing:-1px;line-height:38px}
.main-nav{position:absolute;left:444px;top:24px;display:flex;gap:0}
.main-nav a{font-size:11px;color:var(--purple-dark);text-decoration:none;margin-right:38px}
.header-phone{position:absolute;left:993px;top:15px;width:128px;height:32px;border-radius:16px;background:var(--purple-dark);color:var(--white);font-size:10px;font-weight:600;display:flex;align-items:center;gap:8px;padding-left:8px}
.header-phone .flag{width:20px;height:20px;border-radius:50%;background:var(--purple-soft)}

/* hero */
.hero{position:absolute;left:0;top:62px;width:1200px;height:500px;background:linear-gradient(100deg,#6d4a8e 0%,#8b6aa6 40%,#a190b8 70%,#c9c4d4 100%)}
.hero-photo{position:absolute;left:560px;top:0;width:640px;height:500px;background:linear-gradient(90deg,rgba(120,90,150,0) 0%,rgba(200,195,210,.45) 60%,rgba(150,140,170,.5) 100%)}
.hero-title{position:absolute;left:107px;top:140px;font-family:"Archivo",sans-serif;font-weight:800;font-size:62px;line-height:74px;color:var(--white);letter-spacing:.5px}
.hero-title .mark{color:var(--gold)}
.hero-select{display:inline-flex;align-items:center;gap:20px;vertical-align:middle;margin-left:8px;height:46px;padding:0 22px;border:2px solid var(--white);border-radius:24px;background:rgba(91,42,128,.55);font-size:20px;font-weight:600;position:relative;top:-6px}

/* value band */
.value-band{position:absolute;left:0;top:562px;width:1200px;height:318px;background:linear-gradient(90deg,#6b3596 0%,#5b2a80 55%,#4c1f6e 100%)}
.value-band h2{position:absolute;left:107px;top:78px;width:460px;font-size:38px;line-height:57px;color:var(--white);font-weight:500}
.value-copy{position:absolute;left:612px;top:74px;width:478px;font-size:10px;line-height:15px;color:#efe6f6}
.value-copy p{margin-bottom:14px}

/* empower */
.empower h2{position:absolute;left:100px;top:958px;width:1000px;text-align:center;font-size:30px;line-height:43px;color:var(--purple)}
.benefits{position:absolute;left:195px;top:1160px;list-style:none}
.benefits li{font-size:10px;color:var(--muted);height:28.5px;display:flex;align-items:center;gap:6px}
.benefits b{color:var(--purple);font-weight:700}
.benefits svg{flex:none}
.video-frame{position:absolute;left:612px;top:1115px;width:388px;height:250px;background:linear-gradient(135deg,#2d2f36 0%,#4d5058 45%,#7b7e86 100%)}
.play{position:absolute;left:176px;top:107px;width:36px;height:36px;border-radius:50%;background:var(--purple-mid)}

/* work for */
.work-bg{position:absolute;left:0;top:1440px;width:1200px;height:310px;background:var(--grey)}
.section-title{position:absolute;left:0;width:1200px;text-align:center;font-size:38px;color:var(--purple-dark)}
.slide{position:absolute;left:200px;top:1578px;width:800px;height:344px;background:linear-gradient(180deg,#8b6b5a 0%,#6c5670 55%,#5b3a7e 100%)}
.slide-caption{position:absolute;left:0;bottom:34px;width:100%;text-align:center;color:var(--white)}
.slide-caption h3{font-size:19px;font-weight:500}
.slide-caption p{font-size:10px;line-height:15px;margin-top:6px}
.arrow-btn{position:absolute;width:28px;height:28px;border-radius:50%;border:1px solid #bbb;background:var(--white)}
.dots{position:absolute;left:565px;top:1950px;display:flex;gap:7px}
.dots span{width:6px;height:6px;border-radius:50%;background:#555}

/* talk */
.talk h2{position:absolute;left:0;top:2040px;width:1200px;text-align:center;font-size:38px;color:var(--purple-dark)}
.talk p{position:absolute;left:220px;top:2105px;width:760px;text-align:center;font-size:17px;line-height:26px;color:var(--purple-dark)}
.talk .actions{position:absolute;left:0;top:2186px;width:1200px;display:flex;justify-content:center;gap:16px}
.talk .btn{background:var(--purple-dark)}

/* numbers */
.numbers{position:absolute;left:107px;top:2293px;width:986px;height:405px;background:var(--grey)}
.numbers h2{position:absolute;left:0;top:58px;width:100%;text-align:center;font-size:38px;color:var(--purple-dark)}
.numbers .rule{position:absolute;top:82px;height:1px;width:180px;background:var(--purple)}
.ratio{position:absolute;left:168px;top:142px;font-family:"Archivo",sans-serif;font-weight:600;font-size:196px;line-height:200px;letter-spacing:-6px;background:linear-gradient(90deg,var(--gold-deep) 0%,#c98a3c 40%,#8b4f9a 75%,var(--purple) 100%);-webkit-background-clip:text;background-clip:text;color:transparent}
.numbers .stat{position:absolute;left:481px;top:172px;width:330px;font-size:22px;line-height:32px;color:var(--purple-dark)}
.numbers .btn{position:absolute;left:481px;top:290px}
.chev{position:absolute;top:244px;color:var(--purple-dark);font-size:20px}

/* case studies */
.case{position:absolute;width:388px;height:281px;color:var(--white);text-align:center}
.case h3{position:absolute;left:0;top:184px;width:100%;font-size:19px;line-height:26px;font-weight:500}
.case p{position:absolute;left:0;top:245px;width:100%;font-size:10px}
.case-a{background:linear-gradient(180deg,#6f7a8c 0%,#7d5a8e 60%,#5b2a80 100%)}
.case-b{background:linear-gradient(180deg,#b59a8a 0%,#8f6a8f 60%,#5b2a80 100%)}
.case-c{background:linear-gradient(180deg,#4a3a3a 0%,#5e3e62 60%,#4c1f6e 100%)}
.case-d{background:linear-gradient(180deg,#d6c7cf 0%,#b08aab 55%,#6b3596 100%)}

/* insights */
.insights-bg{position:absolute;left:0;top:3590px;width:1200px;height:530px;background:#f6f5f7}
.post{position:absolute;top:3752px;width:228px;height:228px;background:var(--white);text-align:center}
.post .thumb{height:160px}
.post h4{font-family:"Archivo",sans-serif;font-size:11px;line-height:16px;font-weight:600;color:var(--purple-dark);margin-top:14px;padding:0 26px}
.post .bar{position:absolute;left:104px;bottom:0;width:20px;height:3px;background:var(--purple)}

/* offices */
.map{position:absolute;left:212px;top:4290px;width:790px;height:370px;background:radial-gradient(ellipse at 50% 45%,#d3d9dd 0%,#e4e8ea 55%,#ffffff 80%)}
.offices-divider{position:absolute;left:600px;top:4700px;width:1px;height:180px;background:var(--line)}
.office{position:absolute;top:4720px;width:300px;text-align:center;color:var(--purple-dark)}
.office h3{font-size:19px;font-weight:500}
.office svg{margin:26px auto 6px;display:block}
.office .addr{font-size:10px;line-height:15px}
.office .call{font-size:13px;font-weight:700;margin-top:16px}

/* footer */
.site-footer{position:absolute;left:0;top:4967px;width:1200px;height:362px;background:linear-gradient(90deg,#6e38a0 0%,#5b2a80 50%,#4b1e6d 100%);color:var(--white)}
.site-footer h4{position:absolute;top:72px;font-size:15px;font-weight:500}
.foot-list{position:absolute;top:108px;list-style:none;font-size:10px;line-height:25px;color:#eadff3}
.foot-contact{position:absolute;left:779px;top:108px;font-size:10px}
.social{position:absolute;left:779px;top:138px;width:30px;height:30px;border:1px solid var(--white);border-radius:50%}
.foot-btn{position:absolute;left:779px;height:28px;line-height:28px;border-radius:14px;font-size:10px;font-weight:600;text-align:center;width:130px}
.foot-rule{position:absolute;left:200px;top:325px;width:800px;height:1px;background:rgba(255,255,255,.25)}
.foot-brand{position:absolute;left:200px;top:324px;font-family:"Archivo",sans-serif;font-weight:800;font-size:30px;color:var(--white);letter-spacing:-1px}
.foot-legal{position:absolute;top:338px;font-size:9px;color:#eadff3}
.to-top{position:absolute;left:1085px;top:283px}
</style>
</head>
<body>

<header class="site-header">
  <div class="brand">brevka</div>
  <nav class="main-nav">
    <a href="#">Home</a><a href="#">Clients</a><a href="#">Services</a><a href="#">Case Studies</a><a href="#">Blog</a><a href="#">About Us</a><a href="#">Contact Us</a>
  </nav>
  <div class="header-phone"><span class="flag"></span>⌄ 01632 960 000</div>
</header>

<section class="hero">
  <div class="hero-photo" role="img" aria-label="Photo of two business professionals in discussion at a meeting"></div>
  <h1 class="hero-title"><span class="mark">I</span>DEAL<br>ORIGINATION<br>FOR <span class="hero-select">-- YOU? --<svg width="12" height="8" viewBox="0 0 12 8"><path d="M1 1l5 5 5-5" stroke="#fff" stroke-width="2" fill="none"/></svg></span></h1>
</section>

<section class="value-band">
  <h2>Exclusive Deals, Reduced Risk, Stronger Leverage</h2>
  <div class="value-copy">
    <p>We consistently deliver high-quality deals, bypassing the crowded open market, imagine a pipeline filled with precise targets, aligned with your acquisition goals.</p>
    <p>Our approach minimises execution risk, we bring forward only well-matched prospects backed by transparent tracking and guidance. by specialising in off-market exclusivity, we enhance your negotiation leverage, reducing competition and securing favourable terms for both parties.</p>
    <p>We focus on quality over quantity, building high-trust seller relationships. gain a competitive edge with our deep market knowledge and highly targeted outreach, expanding your network share. brevka enables you to acquire smarter, faster, and more effectively.</p>
  </div>
</section>

<section class="empower">
  <h2>Brevka empowers acquirers to outpace competitors by consistently delivering high-response, off-market deal flow, without adding headcount or overhead.</h2>
  <ul class="benefits">
    <li><svg width="10" height="14" viewBox="0 0 10 14"><path d="M5 0a5 5 0 0 1 5 5c0 3.5-5 9-5 9S0 8.5 0 5a5 5 0 0 1 5-5z" fill="#5b2a80"/></svg><span><b>Find the ideal fit</b> - Target businesses that match your exact criteria</span></li>
    <li><svg width="10" height="14" viewBox="0 0 10 14"><path d="M5 0a5 5 0 0 1 5 5c0 3.5-5 9-5 9S0 8.5 0 5a5 5 0 0 1 5-5z" fill="#5b2a80"/></svg><span><b>More options</b> - Access businesses that aren't publicly listed</span></li>
    <li><svg width="10" height="14" viewBox="0 0 10 14"><path d="M5 0a5 5 0 0 1 5 5c0 3.5-5 9-5 9S0 8.5 0 5a5 5 0 0 1 5-5z" fill="#5b2a80"/></svg><span><b>No noise</b> - Avoid disruption from advisors and brokers</span></li>
    <li><svg width="10" height="14" viewBox="0 0 10 14"><path d="M5 0a5 5 0 0 1 5 5c0 3.5-5 9-5 9S0 8.5 0 5a5 5 0 0 1 5-5z" fill="#5b2a80"/></svg><span><b>Higher-quality deals</b> - Engage with owners who prefer a discreet sale</span></li>
    <li><svg width="10" height="14" viewBox="0 0 10 14"><path d="M5 0a5 5 0 0 1 5 5c0 3.5-5 9-5 9S0 8.5 0 5a5 5 0 0 1 5-5z" fill="#5b2a80"/></svg><span><b>More control</b> - Move at your own pace, without broker pressure</span></li>
    <li><svg width="10" height="14" viewBox="0 0 10 14"><path d="M5 0a5 5 0 0 1 5 5c0 3.5-5 9-5 9S0 8.5 0 5a5 5 0 0 1 5-5z" fill="#5b2a80"/></svg><span><b>Stronger relationships</b> - Direct contact with business owners</span></li>
  </ul>
  <div class="video-frame" role="img" aria-label="Video still of a team working at laptops around a meeting table">
    <svg class="play" viewBox="0 0 36 36"><circle cx="18" cy="18" r="18" fill="#7a3fa8"/><path d="M14 11l11 7-11 7z" fill="#fff"/></svg>
  </div>
</section>

<section class="work-for">
  <div class="work-bg"></div>
  <h2 class="section-title" style="top:1508px">We Work for</h2>
  <div class="slide" role="img" aria-label="Photo of a private equity team meeting in a modern boardroom">
    <div class="slide-caption">
      <h3>Private Equity</h3>
      <p>Expand your pipeline beyond traditional brokers and<br>geographic boundaries</p>
    </div>
  </div>
  <svg class="arrow-btn" style="left:186px;top:1736px" viewBox="0 0 28 28"><circle cx="14" cy="14" r="13.5" fill="#fff" stroke="#bbb"/><path d="M16 9l-5 5 5 5" stroke="#555" fill="none" stroke-width="1.5"/></svg>
  <svg class="arrow-btn" style="left:986px;top:1736px" viewBox="0 0 28 28"><circle cx="14" cy="14" r="13.5" fill="#fff" stroke="#bbb"/><path d="M12 9l5 5-5 5" stroke="#555" fill="none" stroke-width="1.5"/></svg>
  <div class="dots"><span></span><span></span><span></span><span></span><span></span><span></span></div>
</section>

<section class="talk">
  <h2>If you want ideal flow, Let's talk</h2>
  <p>There is only so much you can tell from reviewing our website, the best way to explore is to have a short meeting with one of our team.</p>
  <div class="actions"><a class="btn" href="#">Call: 01632 960 000</a><a class="btn" href="#" style="background:var(--purple)">Contact Brevka</a></div>
</section>

<section class="numbers">
  <div class="rule" style="left:93px"></div>
  <div class="rule" style="left:713px"></div>
  <h2>Brevka the Numbers</h2>
  <span class="chev" style="left:93px">‹</span>
  <div class="ratio">1:5</div>
  <p class="stat">For every 1 target approached, we analyse at least 5 companies</p>
  <a class="btn" href="#">Detailed Analysis</a>
  <span class="chev" style="left:884px">›</span>
</section>

<section class="cases">
  <h2 class="section-title" style="top:2780px">Recent Case Studies</h2>
  <article class="case case-a" style="left:200px;top:2862px" role="img" aria-label="Photo of a fire safety engineer at work">
    <h3>Fire Safety Focussed<br>Investment Group</h3><p>Acquired A bespoke Fire and Security Solutions Business</p>
  </article>
  <article class="case case-b" style="left:612px;top:2862px" role="img" aria-label="Photo of construction workers in hard hats">
    <h3>Leading Labour Recruitment<br>Company</h3><p>Acquired An Established Construction &amp; Recruitment Firm</p>
  </article>
  <article class="case case-c" style="left:200px;top:3170px" role="img" aria-label="Photo of a welder in a workshop">
    <h3>Leading Labour Recruitment<br>Company</h3><p>Acquired An Established Construction &amp; Recruitment Firm</p>
  </article>
  <article class="case case-d" style="left:612px;top:3170px" role="img" aria-label="Photo of fire safety equipment">
    <h3>Fire Safety Focussed<br>Investment Group</h3><p>Acquired A bespoke Fire and Security Solutions Business</p>
  </article>
  <a class="btn abs" href="#" style="left:535px;top:3482px">More Case Studies</a>
</section>

<section class="insights">
  <div class="insights-bg"></div>
  <h2 class="section-title" style="top:3668px">M&amp;A insights &amp; Latest Trends</h2>
  <article class="post" style="left:107px"><div class="thumb" role="img" aria-label="Photo of a handshake over a desk" style="background:linear-gradient(135deg,#c9b9a3,#6e5a4c)"></div><h4>Why off market is key for the motivated buyer</h4><span class="bar"></span></article>
  <article class="post" style="left:360px"><div class="thumb" role="img" aria-label="Photo of a city skyline with location markers" style="background:linear-gradient(180deg,#b9c6d3,#7d6f6a)"></div><h4>Is there a suitable business for sale near me?</h4><span class="bar"></span></article>
  <article class="post" style="left:612px"><div class="thumb" role="img" aria-label="Photo of a glowing growth chart on a screen" style="background:linear-gradient(135deg,#e6eef5,#3d6d9a)"></div><h4>5 Ways to increase your chances of selling your business</h4><span class="bar"></span></article>
  <article class="post" style="left:866px"><div class="thumb" role="img" aria-label="Photo of a person working on finances with a calculator" style="background:linear-gradient(135deg,#e9ecef,#7f8fa3)"></div><h4>How to finance your next business acquisition</h4><span class="bar"></span></article>
  <a class="btn abs" href="#" style="left:548px;top:4015px;background:var(--purple-dark)">View All Blog</a>
</section>

<section class="offices">
  <h2 class="section-title" style="top:4196px">Regional and Cross-Border Deal Makers</h2>
  <div class="map" role="img" aria-label="World map highlighting the UK and Europe region"></div>
  <div class="offices-divider"></div>
  <div class="office" style="left:243px">
    <h3>UK &amp; Europe Office</h3>
    <svg width="18" height="22" viewBox="0 0 18 22"><path d="M9 1a8 8 0 0 1 8 8c0 5-8 12-8 12S1 14 1 9a8 8 0 0 1 8-8z" fill="none" stroke="#5b2a80" stroke-width="1.5"/><circle cx="9" cy="9" r="3" fill="#5b2a80"/></svg>
    <p class="addr">Fourth Floor Meridian Court<br>Reading RG1 9XX</p>
    <p class="call">Call: +44 (0) 1632 960 000</p>
  </div>
  <div class="office" style="left:656px">
    <h3>APAC Office</h3>
    <svg width="18" height="22" viewBox="0 0 18 22"><path d="M9 1a8 8 0 0 1 8 8c0 5-8 12-8 12S1 14 1 9a8 8 0 0 1 8-8z" fill="none" stroke="#5b2a80" stroke-width="1.5"/><circle cx="9" cy="9" r="3" fill="#5b2a80"/></svg>
    <p class="addr">12 Harbour Lane Millers Point<br>NSW 2000 Australia</p>
    <p class="call">Call: +61 (0) 491 570 156</p>
  </div>
</section>

<footer class="site-footer">
  <h4 style="left:200px">Clients</h4>
  <ul class="foot-list" style="left:200px"><li>Private Equity</li><li>Trade Buyers</li><li>Management Buy In</li><li>Search Funds</li><li>Corporate Finance</li></ul>
  <h4 style="left:406px">Services</h4>
  <ul class="foot-list" style="left:406px"><li>Deal Origination</li><li>Single Acquisitions</li><li>Buy and Build</li><li>Bolt-On Acquisitions</li><li>Cross Border/International</li></ul>
  <ul class="foot-list" style="left:587px"><li>Acquisition Finance</li><li>Negotiation Support</li><li>Due Diligence</li></ul>
  <h4 style="left:779px">Contact</h4>
  <p class="foot-contact"><b>Call:</b> +44 (0) 1632 960 000</p>
  <div class="social"></div>
  <div class="foot-btn" style="top:188px;background:var(--purple-mid)">Contact Brevka</div>
  <div class="foot-btn" style="top:222px;background:var(--gold);color:var(--purple-dark)">Book Appointment</div>
  <svg class="to-top" width="18" height="22" viewBox="0 0 18 22"><path d="M9 1l8 20-8-6-8 6z" fill="#f2b705"/></svg>
  <div class="foot-rule"></div>
  <div class="foot-brand">brevka</div>
  <p class="foot-legal" style="left:306px">© 2025 <b>Brevka Limited.</b> All rights reserved</p>
  <p class="foot-legal" style="left:587px">Terms of Use &nbsp; | &nbsp; Privacy Policy &nbsp; | &nbsp; Contact Us</p>
</footer>

</body>
</html>
```